Business Card Design

Provide project management services to the construction and other industries
Construction services - Civil and Concrete works
Shop Detailing
Structural Modelling
Client side coordination of project teams and consultants
Feasibility Studies for construction projects

Industry/Entity Type

Business

Contact Information for Business Card

Crestline Ops
Darrel Pikett B.Eng (Hons), G.C.Bus.
Director

m: 0412 583 716
e: dpikett@crestlineops.com.au

p: 08 6293 4078
a: 17 Bramblewood Court, Stirling, WA 6021

```html
<!DOCTYPE html>
<html lang="en">
<head>
<meta charset="utf-8">
<title>Crestline Ops – Business Card</title>
<link rel="stylesheet" href="https://fonts.googleapis.com/css2?family=Lato:wght@400;700;900&display=swap">
<style>
  :root {
    --green: #0f8a1c;
    --green-dark: #0a6e15;
    --white: #ffffff;
    --paper: #f4f4f4;
    --ink: #111111;
    --muted: #333333;
    --backdrop: #2a2a2a;
  }
  * { box-sizing: border-box; margin: 0; padding: 0; }
  html, body {
    width: 1200px; height: 873px; overflow: hidden;
    background: var(--backdrop);
    font-family: "Lato", Arial, sans-serif;
  }
  .stage {
    position: relative; width: 1200px; height: 873px;
    display: flex; align-items: center; justify-content: center; gap: 40px;
  }
  .card {
    position: relative; width: 540px; height: 310px;
    border-radius: 22px; overflow: hidden;
  }

  /* Back side */
  .card--back { background: var(--green); color: var(--white); padding: 58px 48px; }
  .card--back .brand {
    font-weight: 900; font-size: 50px; letter-spacing: 2px; line-height: 1;
    text-transform: uppercase; color: var(--white);
  }
  .services { list-style: none; margin: 30px 0 0 10px; }
  .services li {
    display: flex; align-items: center; gap: 10px;
    font-size: 15px; line-height: 1; margin-bottom: 9px;
  }
  .services svg { width: 17px; height: 17px; flex: none; }

  /* Front side */
  .card--front { background: var(--paper); text-align: center; }
  .person { padding-top: 30px; }
  .person__name { color: var(--green); font-weight: 700; font-size: 20px; }
  .person__quals { color: var(--muted); font-size: 13px; margin-top: 3px; }
  .person__role { color: var(--muted); font-weight: 700; font-size: 12px; margin-top: 2px; }
  .card--front .brand {
    margin-top: 34px; font-weight: 900; font-size: 40px; letter-spacing: 1px;
    text-transform: uppercase; color: var(--ink);
  }
  .contacts {
    display: grid; grid-template-columns: auto auto; justify-content: center;
    column-gap: 34px; row-gap: 10px; margin-top: 30px; text-align: left;
  }
  .contact { display: flex; align-items: center; gap: 9px; font-size: 16px; color: var(--muted); }
  .contact--email { grid-column: 1 / span 2; }
  .contact svg { width: 24px; height: 24px; flex: none; }
  .address-band {
    position: absolute; left: 0; right: 0; bottom: 0; height: 40px;
    background: var(--green); color: var(--white);
    font-weight: 700; font-size: 16px; letter-spacing: .3px;
    display: flex; align-items: center; justify-content: center;
  }
</style>
</head>
<body>
<main class="stage">

  <section class="card card--back" aria-label="Card back">
    <div class="brand">Crestline Ops</div>
    <ul class="services">
      <li><svg viewBox="0 0 20 20"><circle cx="10" cy="10" r="9" fill="#fff"/><path d="M5.5 10.5l3 3 6-6.5" fill="none" stroke="var(--green)" stroke-width="2.4" stroke-linecap="round" stroke-linejoin="round"/></svg>Shop Detailing</li>
      <li><svg viewBox="0 0 20 20"><circle cx="10" cy="10" r="9" fill="#fff"/><path d="M5.5 10.5l3 3 6-6.5" fill="none" stroke="var(--green)" stroke-width="2.4" stroke-linecap="round" stroke-linejoin="round"/></svg>Structural Modelling</li>
      <li><svg viewBox="0 0 20 20"><circle cx="10" cy="10" r="9" fill="#fff"/><path d="M5.5 10.5l3 3 6-6.5" fill="none" stroke="var(--green)" stroke-width="2.4" stroke-linecap="round" stroke-linejoin="round"/></svg>Civil &amp; Concrete works</li>
      <li><svg viewBox="0 0 20 20"><circle cx="10" cy="10" r="9" fill="#fff"/><path d="M5.5 10.5l3 3 6-6.5" fill="none" stroke="var(--green)" stroke-width="2.4" stroke-linecap="round" stroke-linejoin="round"/></svg>Feasibility Studies for construction projects</li>
      <li><svg viewBox="0 0 20 20"><circle cx="10" cy="10" r="9" fill="#fff"/><path d="M5.5 10.5l3 3 6-6.5" fill="none" stroke="var(--green)" stroke-width="2.4" stroke-linecap="round" stroke-linejoin="round"/></svg>Client Side coordination of project teams &amp; consultants</li>
    </ul>
  </section>

  <section class="card card--front" aria-label="Card front">
    <div class="person">
      <div class="person__name">Darrel Pikett</div>
      <div class="person__quals">B.Eng (Hons), G.C.Bus.</div>
      <div class="person__role">Director</div>
    </div>
    <div class="brand">Crestline Ops</div>
    <div class="contacts">
      <div class="contact contact--mobile">
        <svg viewBox="0 0 24 24"><circle cx="12" cy="12" r="12" fill="var(--green)"/><path d="M8.6 6.5l1.8-.4 1.1 3-1.2.9c.6 1.5 1.6 2.6 3 3.3l1-1.1 2.9 1.2-.4 1.9c-4.6.4-8.6-3.9-8.2-8.8z" fill="#fff"/></svg>
        0412 583 716
      </div>
      <div class="contact contact--phone">
        <svg viewBox="0 0 24 24"><circle cx="12" cy="12" r="12" fill="var(--green)"/><rect x="8.5" y="6" width="7" height="3.5" fill="#fff"/><rect x="6" y="9.5" width="12" height="5.5" rx="1" fill="#fff"/><rect x="8.5" y="13" width="7" height="5" fill="#fff" stroke="var(--green)" stroke-width="1"/></svg>
        08 6293 4078
      </div>
      <div class="contact contact--email">
        <svg viewBox="0 0 24 24"><circle cx="12" cy="12" r="12" fill="var(--green)"/><rect x="6" y="8" width="12" height="8.5" fill="#fff"/><path d="M6 8l6 5 6-5" fill="none" stroke="var(--green)" stroke-width="1.3"/></svg>
        dpikett@crestlineops.com.au
      </div>
    </div>
    <div class="address-band">17 Bramblewood Court, Stirling, WA 6021</div>
  </section>

</main>
</body>
</html>
```